Brexmoor Solutions
Not Necessary
Simple
Marlon Teague
N/A
marlon@brexmoorsolutions.example
http://www.brexmoorsolutions.example
Brexmoor Solutions is a custom development/software development firm. Specialize on web and mobile development.
I'd be interested in what a double sided business card looks like but may settle on a one-sided card.
Your discretion on whether to use logo's font or another - whatever looks best.
Logo and fonts

```html
<!DOCTYPE html>
<html lang="en">
<head>
<meta charset="UTF-8">
<title>Brexmoor Solutions – Business Card</title>
<link href="https://fonts.googleapis.com/css2?family=Titillium+Web:wght@400;600;700&display=swap" rel="stylesheet">
<style>
  :root {
    --stage: #e4e6e9;
    --card: #ffffff;
    --brand-blue: #1f6fb4;
    --brand-blue-dark: #16568f;
    --ink: #3a3f45;
    --muted: #7c838b;
    --band-grey: #d4d7db;
    --band-grey-dark: #9da2a8;
  }
  * { box-sizing: border-box; margin: 0; padding: 0; }
  html, body { width: 1200px; height: 682px; overflow: hidden; }
  body {
    background: var(--stage);
    font-family: "Titillium Web", sans-serif;
    display: flex;
    align-items: center;
    justify-content: center;
    gap: 48px;
  }
  .card {
    position: relative;
    width: 540px;
    height: 309px;
    background: var(--card);
    box-shadow: 0 6px 18px rgba(0,0,0,.12);
    overflow: hidden;
  }
  .wordmark {
    color: var(--brand-blue);
    font-weight: 700;
    line-height: 1;
    letter-spacing: .5px;
  }
  /* back side */
  .card--back .wordmark {
    position: absolute;
    left: 0; right: 0;
    top: 112px;
    text-align: center;
    font-size: 40px;
  }
  .card--back .web {
    position: absolute;
    left: 0; right: 0;
    top: 168px;
    text-align: center;
    font-size: 15px;
    font-weight: 600;
    color: var(--ink);
    letter-spacing: 1px;
  }
  .card--back .accent {
    position: absolute;
    left: 48px; top: 48px;
    width: 120px; height: 120px;
    background: var(--brand-blue);
    opacity: .06;
  }
  /* front side */
  .card--front .wordmark {
    position: absolute;
    right: 40px;
    top: 58px;
    font-size: 32px;
    text-align: right;
  }
  .person {
    position: absolute;
    left: 64px;
    top: 200px;
    display: flex;
    align-items: baseline;
    gap: 28px;
  }
  .person__name { font-size: 17px; font-weight: 700; color: var(--brand-blue); }
  .person__title { font-size: 11px; color: var(--muted); }
  .contact {
    position: absolute;
    left: 280px;
    top: 184px;
    list-style: none;
    font-size: 11px;
    color: var(--muted);
  }
  .contact li { display: flex; align-items: center; gap: 7px; margin-bottom: 5px; }
  .contact svg { width: 12px; height: 12px; flex: none; }
  .band { position: absolute; left: 0; bottom: 0; width: 540px; height: 74px; }
  .band__web {
    position: absolute;
    right: 14px;
    bottom: 18px;
    line-height: 16px;
    font-size: 11px;
    font-weight: 600;
    color: #fff;
    letter-spacing: .4px;
    white-space: nowrap;
  }
</style>
</head>
<body>

  <section class="card card--back" aria-label="Card back">
    <div class="accent"></div>
    <div class="wordmark">Brexmoor Solutions</div>
    <div class="web">www.brexmoorsolutions.example</div>
  </section>

  <section class="card card--front" aria-label="Card front">
    <div class="wordmark">Brexmoor Solutions</div>

    <div class="person">
      <span class="person__name">Marlon Teague</span>
      <span class="person__title">N/A</span>
    </div>

    <ul class="contact">
      <li>
        <svg viewBox="0 0 12 12"><circle cx="6" cy="6" r="6" fill="var(--muted)"/><rect x="4" y="2.5" width="4" height="7" rx="1" fill="#fff"/></svg>
        555-014-0392
      </li>
      <li>
        <svg viewBox="0 0 12 12"><circle cx="6" cy="6" r="6" fill="var(--muted)"/><rect x="2.8" y="3.8" width="6.4" height="4.4" fill="#fff"/><path d="M2.8 3.8 6 6.3 9.2 3.8" stroke="var(--muted)" stroke-width=".8" fill="none"/></svg>
        marlon@brexmoorsolutions.example
      </li>
    </ul>

    <svg class="band" viewBox="0 0 540 74" preserveAspectRatio="none">
      <polygon points="300,62 540,62 540,32 318,32" fill="var(--band-grey)"/>
      <polygon points="322,58 540,58 540,38 336,38" fill="var(--band-grey-dark)"/>
      <polygon points="0,62 540,62 540,74 0,74" fill="var(--brand-blue)"/>
      <polygon points="0,66 300,66 320,74 0,74" fill="var(--brand-blue-dark)"/>
    </svg>
    <div class="band__web">www.brexmoorsolutions.example</div>
  </section>

</body>
</html>
```